Business Card Re-Design for a Lighting Designer

I would like my business card re-designed. It is currently high gloss and they scratch too easily. I don not think the current design lends itself well to a matte finish. I have included the current design for reference along with our company logo.
Check out our website for current branding.
http://www.brambleorchidstudio.example

Updates
Some of the top contenders are muslim and it is a holiday for them. I do not want to discriminate and would expect the same courtesy for holidays we celebrate.
Target Market(s)
Interior Designers, Architects
Contact Information for Business Card
Logo - Name, Title, Address, Telephone Number and Extension, Email
Font styles to use
Requirements
Must have
- All the information listed on the current business card. If you use Red, it needs to be the red from our logo.
Nice to have
- Vertical and Horizontal Designs will be entertained.
Should not have
- Requirements for a glossy finish...should not look too corporate since we are a design firm.

```html
<!DOCTYPE html>
<html lang="en">
<head>
<meta charset="utf-8">
<title>Bramble Orchid Studio – Business Card</title>
<link href="https://fonts.googleapis.com/css2?family=Cabin:wght@400;500;600&family=Cinzel:wght@700&display=swap" rel="stylesheet">
<style>
  :root {
    --brand-red: #990000;
    --stripe-grey: #999999;
    --stripe-black: #000000;
    --ink: #111111;
    --muted: #8a8a8a;
    --paper: #ffffff;
    --page: #ffffff;
  }
  html, body {
    margin: 0;
    width: 1200px;
    height: 1200px;
    overflow: hidden;
    background: var(--page);
  }
  .canvas {
    position: relative;
    width: 1200px;
    height: 1200px;
  }
  .card {
    position: absolute;
    top: 452px;
    width: 516px;
    height: 295px;
    background: var(--paper);
    border: 1px solid #000;
    box-sizing: border-box;
    box-shadow: 0 10px 22px rgba(0,0,0,0.18);
    overflow: hidden;
    font-family: "Cabin", sans-serif;
    color: var(--ink);
  }
  .card--front { left: 55px; }
  .card--back { left: 630px; }

  .card__bands {
    position: absolute;
    inset: 0;
  }

  .holder {
    position: absolute;
    left: 28px;
    top: 56px;
  }
  .holder__name {
    margin: 0;
    font-family: "Cinzel", serif;
    font-weight: 700;
    font-size: 14.5px;
    letter-spacing: 0.2px;
    color: var(--brand-red);
    line-height: 1;
  }
  .holder__title {
    margin: 5px 0 0;
    font-size: 10.5px;
    font-weight: 500;
    color: var(--brand-red);
    letter-spacing: 0.3px;
  }

  .address {
    position: absolute;
    left: 28px;
    top: 143px;
    margin: 0;
    font-style: normal;
    font-size: 9.6px;
    font-weight: 500;
    line-height: 12.5px;
  }

  .contacts {
    position: absolute;
    left: 28px;
    top: 182px;
    margin: 0;
    padding: 0;
    list-style: none;
    font-size: 9.6px;
    font-weight: 500;
  }
  .contacts li {
    display: flex;
    align-items: center;
    height: 15.5px;
  }
  .contacts svg {
    width: 10px;
    height: 10px;
    margin-right: 6px;
    fill: var(--brand-red);
  }

  .wordmark {
    position: absolute;
    display: flex;
    align-items: flex-start;
    gap: 10px;
    font-family: "Cabin", sans-serif;
    font-weight: 400;
    color: var(--ink);
    font-size: 27px;
    line-height: 27px;
  }
  .wordmark__square {
    width: 40px;
    height: 40px;
    background: var(--brand-red);
    flex: none;
    margin-top: 3px;
  }
  .wordmark__name { margin: 0; }
  .card--front .wordmark { left: 320px; top: 86px; }
  .card--back .wordmark { left: 150px; top: 106px; }
</style>
</head>
<body>
<main class="canvas">

  <section class="card card--front" aria-label="Business card front">
    <svg class="card__bands" viewBox="0 0 516 295" aria-hidden="true">
      <rect x="0" y="0" width="516" height="28" fill="var(--brand-red)"/>
      <polygon points="358,0 410,0 387,28 334,28" fill="var(--stripe-grey)"/>
      <polygon points="410,0 460,0 440,28 387,28" fill="var(--stripe-black)"/>
      <rect x="0" y="266" width="260" height="10" fill="var(--stripe-grey)"/>
      <rect x="0" y="276" width="516" height="19" fill="var(--brand-red)"/>
      <path d="M250,276 C262,262 272,253 288,253 L516,253 L516,295 L250,295 Z" fill="var(--brand-red)"/>
    </svg>

    <header class="holder">
      <h1 class="holder__name">Maren Holloway</h1>
      <p class="holder__title">PRINCIPAL</p>
    </header>

    <address class="address">
      217 Larkspur Row Suite 40<br>
      Portland, Oregon 97205 USA
    </address>

    <ul class="contacts">
      <li>
        <svg viewBox="0 0 10 10" aria-hidden="true"><path d="M1,3.2 C1,1.8 3,1 5,1 C7,1 9,1.8 9,3.2 L7.2,3.8 L6.8,2.8 L3.2,2.8 L2.8,3.8 Z M2.5,4.3 L7.5,4.3 L8.5,9 L1.5,9 Z"/></svg>
        555.014.2290
      </li>
      <li>
        <svg viewBox="0 0 10 10" aria-hidden="true"><path d="M0.5,2 L9.5,2 L9.5,8 L0.5,8 Z M1.2,2.6 L5,5.6 L8.8,2.6 L8.8,2.9 L5,6.3 L1.2,2.9 Z" fill-rule="evenodd"/></svg>
        info@brambleorchidstudio.example
      </li>
      <li>
        <svg viewBox="0 0 10 10" aria-hidden="true"><circle cx="5" cy="5" r="4.2" fill="none" stroke="var(--brand-red)" stroke-width="1.1"/><path d="M5,5 L5,1 A4,4 0 0 1 8.5,6.5 Z M2.2,4 L4,5.5 L3,8 Z"/></svg>
        www.brambleorchidstudio.example
      </li>
    </ul>

    <div class="wordmark">
      <span class="wordmark__square" aria-hidden="true"></span>
      <p class="wordmark__name">Bramble<br>Orchid<br>Studio</p>
    </div>
  </section>

  <section class="card card--back" aria-label="Business card back">
    <div class="wordmark">
      <span class="wordmark__square" aria-hidden="true"></span>
      <p class="wordmark__name">Bramble<br>Orchid<br>Studio</p>
    </div>
  </section>

</main>
</body>
</html>
```